Magician | Speaker looks for an innovative business card design

I'm a magician and public speaker offering artistic and modern magical experiences.
I'm based in Brussels (Belgium.) I love magic performed up-close, creating a space of intimacy, even when I'm on stage.
The final design should communicate professionalism, elegance, artistry, and a friendly kind personality

I would like to see designs based either on my photos and/or the way I sign my name Theo Varn (see attached files for more info.)
Additional photos and more info about what I offer can be seen at www.theo-varn.net

My current business card design is also attached. I like the fact that the reverse of my current design includes quotes from master magicians about magic, changing the way my participants see the art of magic.

Note: I would like a double-sided card design. However, I need white space on the reverse to be able to write things on for my performances.

Details to include on the card:
Artist name: Theo Varn
Offer: magician + (public) speaker or magic + (public) speaking (the + sign can be replaced by another character, like a bullet or a pipe)
Phone: +32 471 236 519
Email: book@theo-varn.net
(optional) Website: www.theo-varn.net or theo-varn.net

Target Market(s)

Corporate, organisations, companies as well as individuals

Industry/Entity Type

Artists

Colors

Designer to choose colors to be used in the design.

Requirements
Nice to have
• A side with a mirror could be nice

```html
<!DOCTYPE html>
<html lang="en">
<head>
<meta charset="utf-8">
<title>Theo Varn – Magician &amp; Speaker Business Card</title>
<link rel="stylesheet" href="https://fonts.googleapis.com/css2?family=Allura&family=Tinos:ital,wght@0,400;0,700;1,400&display=swap">
<style>
  :root {
    --ink: #050507;
    --paper: #ffffff;
    --photo-light: #7c8192;
    --photo-mid: #4a4e5e;
    --photo-dark: #15161c;
    --rule: #ffffff;
  }
  html, body {
    margin: 0;
    padding: 0;
    overflow: hidden;
    background: var(--ink);
  }
  .card {
    position: relative;
    width: 1200px;
    height: 686px;
    overflow: hidden;
    background: var(--ink);
    color: var(--paper);
    font-family: "Tinos", "Times New Roman", serif;
  }
  .card__photo {
    position: absolute;
    left: 230px;
    top: 0;
    width: 970px;
    height: 686px;
    background:
      radial-gradient(ellipse 320px 300px at 480px 420px, var(--photo-light) 0%, rgba(124,129,146,0) 100%),
      linear-gradient(90deg, var(--ink) 0%, var(--photo-dark) 18%, var(--photo-mid) 55%, var(--photo-dark) 100%);
  }
  .top-rule {
    position: absolute;
    left: 0; top: 0;
    width: 238px; height: 2px;
    background: var(--rule);
  }
  .quote {
    position: absolute;
    left: 30px;
    top: 40px;
    margin: 0;
    font-family: "Allura", cursive;
    font-size: 42px;
    line-height: 46px;
    font-weight: 400;
  }
  .quote__author {
    position: absolute;
    left: 35px;
    top: 242px;
    margin: 0;
    font-size: 17px;
    line-height: 22px;
    letter-spacing: 0.3px;
  }
  .quote__author span { display: block; text-transform: uppercase; }
  .quote__author em { display: block; font-style: italic; }
  .rule {
    position: absolute;
    height: 2px;
    background: var(--rule);
    top: 529px;
  }
  .rule--left { left: 0; width: 479px; }
  .rule--right { left: 850px; width: 350px; }
  .website {
    position: absolute;
    left: 32px;
    top: 580px;
    font-size: 30px;
    font-weight: 700;
  }
  .name {
    position: absolute;
    right: 36px;
    top: 150px;
    margin: 0;
    font-family: "Allura", cursive;
    font-weight: 400;
    font-size: 150px;
    line-height: 1;
    white-space: nowrap;
  }
  .offer {
    position: absolute;
    right: 44px;
    top: 490px;
    margin: 0;
    font-size: 26px;
    font-weight: 700;
    font-variant: small-caps;
  }
  .contact {
    position: absolute;
    right: 44px;
    top: 544px;
    margin: 0;
    text-align: right;
    font-size: 30px;
    font-weight: 700;
    line-height: 36px;
    font-style: normal;
  }
  .contact span { display: block; }
</style>
</head>
<body>
  <div class="card">
    <div class="card__photo" role="img" aria-label="Black and white photo of the magician laughing in front of a brick wall, surrounded by floating soap bubbles"></div>
    <div class="top-rule"></div>

    <blockquote class="quote">“Magic is not about fooling<br>and deceiving people.<br>It is about giving them<br>energy, delight and wonder”</blockquote>
    <p class="quote__author"><span>Martin Elbe</span><em>Master magician</em></p>

    <h1 class="name">Theo Varn</h1>
    <p class="offer">Magician - Speaker</p>

    <div class="rule rule--left"></div>
    <div class="rule rule--right"></div>

    <div class="website">www.theo-varn.net</div>
    <address class="contact">
      <span>+32 471 236 519</span>
      <span>book@theo-varn.net</span>
    </address>
  </div>
</body>
</html>
```